2 Company Culture Posters

We need 2 Internal posters designed for a company meeting that states:
1) Our Mission, Vision, Why
2) Our Core Values

Posters size: 24" W x 36" H

Attaching:
-logo
-logo color palette
-look and feel (mood board)
-mission, vision and why statements
-core values

Industry/Entity Type

It Company

```html
<!DOCTYPE html>
<html lang="en">
<head>
<meta charset="utf-8">
<title>Vision. Mission. Why — Harbor Lane Lending</title>
<link rel="stylesheet" href="https://fonts.googleapis.com/css2?family=Bebas+Neue&family=Roboto+Condensed:wght@400;700&display=swap">
<style>
  :root {
    --paper: #ffffff;
    --ink: #231f20;
    --accent: #5bc3dc;
    --rule: #3a3a3a;
    --photo-sky: #9aa3ad;
    --photo-warm: #c98a4a;
    --photo-ground: #2f3520;
  }
  * { margin: 0; padding: 0; box-sizing: border-box; }
  html, body { width: 800px; height: 1200px; overflow: hidden; background: var(--paper); }
  .poster {
    position: relative;
    width: 800px;
    height: 1200px;
    background: var(--paper);
    color: var(--ink);
    font-family: "Roboto Condensed", "Arial Narrow", sans-serif;
  }
  .brand {
    position: absolute;
    top: 32px;
    right: 36px;
    text-align: right;
    color: var(--ink);
  }
  .brand-name {
    font-family: "Roboto Condensed", "Arial Narrow", sans-serif;
    font-weight: 700;
    font-size: 22px;
    letter-spacing: -0.5px;
    line-height: 1;
  }
  .brand-tagline {
    font-size: 8px;
    line-height: 1;
    margin-top: 2px;
  }
  .headline {
    position: absolute;
    left: 107px;
    top: 196px;
    width: 586px;
    font-family: "Bebas Neue", "Oswald", sans-serif;
    font-weight: 400;
    font-size: 98px;
    line-height: 1;
    color: var(--accent);
    white-space: nowrap;
    letter-spacing: -0.5px;
  }
  .headline-rule {
    position: absolute;
    left: 107px;
    top: 287px;
    width: 586px;
    height: 1px;
    background: var(--rule);
  }
  .statements {
    position: absolute;
    left: 107px;
    top: 318px;
    width: 586px;
    font-size: 16.5px;
    line-height: 24.5px;
  }
  .statement { text-align: justify; margin-bottom: 26px; }
  .statement-label { font-weight: 700; }
  .cityscape {
    position: absolute;
    left: 0;
    top: 800px;
    width: 800px;
    height: 400px;
    display: block;
  }
</style>
</head>
<body>
<main class="poster">
  <header class="brand">
    <div class="brand-name">Harbor Lane Lending</div>
    <div class="brand-tagline">Smarter Loans for Residential Investors</div>
  </header>

  <h1 class="headline">Vision. Mission. Why</h1>
  <div class="headline-rule"></div>

  <section class="statements">
    <p class="statement"><span class="statement-label">VISION:</span> Help customers prosper and communities flourish.</p>
    <p class="statement"><span class="statement-label">MISSION:</span> Optimize customer success and build trusted partnerships.<br>
    Our customer obsession is expressed through a collaborative approach that provides access to our people, resources, relationships and exclusive real estate investment opportunities. Together, we revitalize properties, create move-in ready homes and invigorate communities.</p>
    <p class="statement"><span class="statement-label">WHY:</span> We are excited about working with real estate entrepreneurs. Every property purchase and renovation reflect a piece of the American Dream to our clients and the communities they serve. We add value beyond lending by openly sharing our knowledge and resources. We want our customers to have every opportunity for success because when they succeed, communities win.</p>
  </section>

  <svg class="cityscape" viewBox="0 0 800 400" role="img" aria-label="Photograph of a row of painted Victorian houses at dusk with a downtown city skyline behind them">
    <defs>
      <linearGradient id="cityscape-tone" x1="0" y1="0" x2="0" y2="1">
        <stop offset="0" stop-color="var(--photo-sky)"/>
        <stop offset="0.35" stop-color="#7f7668"/>
        <stop offset="0.7" stop-color="var(--photo-warm)"/>
        <stop offset="1" stop-color="var(--photo-ground)"/>
      </linearGradient>
    </defs>
    <rect x="0" y="0" width="800" height="400" fill="url(#cityscape-tone)"/>
  </svg>
</main>
</body>
</html>
```